Atelier Marrow Architecture business card

We need to update our business card. We do high end custom residential, hospitality, and wellness architecture. We focus on creating unique spaces and design around the five senses, believing that architecture's true impact is not on our surroundings, but within us. We would like to see designs are instill a sense of calm awe. They should be crisp, fresh, clean, authentic, & contemporary without being sterile, overworked, or harsh. White space is important. Alternative materials are an option if natural. We have created our own logo and would like designs to incorporate it. However, we are willing to see alternatives if the logo becomes a stumbling block and you have an alternate you suggest. Card must have the following information:
Atelier Marrow Architecture, Inc.
728 Holloway Ct. NE Atlanta, GA 30318
Marcus T. Whitcombe, AIA, NCARB, LEED AP BD+C
ateliermarrow.example

Target Market(s)

Higher net worth individuals with an appreciation for design, nature, sustainability,

Industry/Entity Type

Architect

Contact Information for Business Card

See above. The title of Owner or Architect is helpful but not necessary. Minimalism should trump additional information.

Font styles to use
Serif
Sans Serif

Requirements
Must have
• It should look professional. It must use logo
Should not have
• caligraphy, animals, anything that is cute,

```html
<!DOCTYPE html>
<html lang="en">
<head>
<meta charset="utf-8">
<title>Atelier Marrow Architecture – Business Card</title>
<link rel="stylesheet" href="https://fonts.googleapis.com/css2?family=Roboto:wght@300;400;500&display=swap">
<style>
  :root {
    --canvas: #e6e6e6;
    --card-dark: #3a3938;
    --card-light: #ffffff;
    --ink-light: #f2f2f2;
    --ink-dark: #3b3b3b;
    --accent: #1e7a3c;
    --shadow: rgba(0, 0, 0, 0.12);
  }
  * { box-sizing: border-box; margin: 0; padding: 0; }
  html, body {
    width: 1167px;
    height: 1200px;
    overflow: hidden;
    background: var(--canvas);
    font-family: "Roboto", Arial, sans-serif;
  }
  .sheet {
    position: relative;
    width: 1167px;
    height: 1200px;
  }
  .card {
    position: absolute;
    left: 163px;
    width: 840px;
    height: 480px;
    box-shadow: 0 8px 24px var(--shadow);
  }
  .card--front {
    top: 90px;
    background: var(--card-dark);
    display: flex;
    align-items: center;
    justify-content: center;
  }
  .brand-name {
    color: var(--ink-light);
    font-weight: 300;
    font-size: 34px;
    letter-spacing: 0.22em;
    text-transform: uppercase;
    text-align: center;
    line-height: 1.5;
  }
  .card--back {
    top: 630px;
    background: var(--card-light);
  }
  .holder {
    position: absolute;
    right: 470px;
    top: 236px;
    text-align: right;
  }
  .holder__name {
    color: var(--accent);
    font-weight: 500;
    font-size: 34px;
    letter-spacing: 0.01em;
  }
  .holder__credentials {
    color: var(--ink-dark);
    font-size: 15px;
    margin-top: 6px;
    letter-spacing: 0.03em;
  }
  .divider {
    position: absolute;
    left: 390px;
    top: 150px;
    width: 2px;
    height: 170px;
    background: var(--accent);
  }
  .contact {
    position: absolute;
    left: 412px;
    top: 150px;
    color: var(--ink-dark);
    font-size: 15px;
    line-height: 1.45;
  }
  .contact__address { margin-bottom: 14px; }
  .contact__list { list-style: none; }
  .contact__item {
    display: flex;
    align-items: center;
    gap: 10px;
    margin-bottom: 4px;
  }
  .contact__icon { width: 16px; height: 16px; flex: none; }
</style>
</head>
<body>
<main class="sheet">
  <section class="card card--front">
    <p class="brand-name">Atelier Marrow<br>Architecture</p>
  </section>

  <section class="card card--back">
    <div class="holder">
      <p class="holder__name">Marcus T. Whitcombe</p>
      <p class="holder__credentials">AIA, NCARB, LEED AP BD+C</p>
    </div>
    <div class="divider"></div>
    <div class="contact">
      <p class="contact__address">728 Holloway Ct. NE<br>Atlanta, GA 30318</p>
      <ul class="contact__list">
        <li class="contact__item">
          <svg class="contact__icon" viewBox="0 0 16 16" aria-hidden="true">
            <circle cx="8" cy="8" r="7" fill="none" stroke="#1e7a3c" stroke-width="1.4"/>
            <path d="M5.5 4.8c.4-.4.9-.3 1.1.1l.6 1.2c.2.4 0 .7-.3.9l-.4.3c.4.9 1.1 1.6 2 2l.3-.4c.2-.3.5-.5.9-.3l1.2.6c.4.2.5.7.1 1.1-.8.8-2 .9-3.3 0-1-.7-1.8-1.5-2.4-2.5-.7-1.2-.6-2.3.2-3z" fill="#1e7a3c"/>
          </svg>
          <span>404 555 0187</span>
        </li>
        <li class="contact__item">
          <svg class="contact__icon" viewBox="0 0 16 16" aria-hidden="true">
            <rect x="1.5" y="3.5" width="13" height="9" fill="#1e7a3c"/>
            <path d="M1.5 3.5l6.5 5 6.5-5" fill="none" stroke="#ffffff" stroke-width="1.2"/>
          </svg>
          <span>info@ateliermarrow.example</span>
        </li>
        <li class="contact__item">
          <svg class="contact__icon" viewBox="0 0 16 16" aria-hidden="true">
            <circle cx="8" cy="8" r="7" fill="#1e7a3c"/>
            <ellipse cx="8" cy="8" rx="3" ry="7" fill="none" stroke="#ffffff" stroke-width="1"/>
            <path d="M1 8h14M2.2 4.5h11.6M2.2 11.5h11.6" stroke="#ffffff" stroke-width="1"/>
          </svg>
          <span>www.ateliermarrow.example</span>
        </li>
      </ul>
    </div>
  </section>
</main>
</body>
</html>
```